Health and Safety Consultant to the In the renewables wind farm construction industry (OFFSHORE WIND/OIL AND GAS)
APPOINTED PERSON HEAVY LIFTING OPERATIONS.
Lift plan preperations
marcus_dellow@brightmail.example
Tel 07712948305
14 GLANMORE AVE, DENBIGHSHIRE NORTH WALES
LL93 4QX
APPOINTED PERSON HEAVY LIFTING OPERATIONS.Health and Safety Consultant to the In the renewables wind farm construction industry (OFFSHORE WIND/OIL AND GAS)

Target Market(s)

Offshore professionals

Industry/Entity Type

Construction

Contact Information for Business Card

M.D.HEALTH AND SAFETY SERVICES LTD
Tel 07712948305
14 Glanmore Ave, Marrowdale West Coast ll934qx

Font styles to use
Serif
Sans Serif

Requirements
Must have
• HIGH QUALITY PLASTIC OR SIMILAR MATERIALS USED
Nice to have
• QUALITY LOGO I HAVE ATTACHED A LOGO BELOW BUT I'M OPENT TO DESIGN CHANGE

```html
<!DOCTYPE html>
<html lang="en">
<head>
<meta charset="utf-8">
<title>Harbourline Lift Safety Ltd – Business Card</title>
<link rel="stylesheet" href="https://fonts.googleapis.com/css2?family=Tenor+Sans&display=swap">
<style>
  :root {
    --page-bg: #dfe3e6;
    --card-clear: #eef2f3;
    --panel-top: #1f4f9e;
    --panel-mid: #2a8a72;
    --panel-low: #245f66;
    --panel-bottom: #1a3466;
    --divider: #a4a8a6;
    --brand-ink: #2c3b7c;
    --name-ink: #cfe070;
    --detail-ink: #eadca2;
  }
  * { margin: 0; padding: 0; box-sizing: border-box; }
  html, body {
    width: 1200px;
    height: 926px;
    overflow: hidden;
    background: var(--page-bg);
    font-family: "Tenor Sans", sans-serif;
  }
  .business-card {
    position: absolute;
    left: 120px;
    top: 189px;
    width: 960px;
    height: 548px;
    background: var(--card-clear);
    border-radius: 6px;
    overflow: hidden;
    box-shadow: 0 10px 30px rgba(30, 40, 60, 0.18);
  }
  .card-art {
    position: absolute;
    inset: 0;
    width: 960px;
    height: 548px;
  }
  .brand {
    position: absolute;
    left: 30px;
    top: 140px;
    width: 340px;
    text-align: center;
    color: var(--brand-ink);
  }
  .brand-dot {
    display: block;
    width: 58px;
    height: 58px;
    margin: 0 auto 22px;
    border-radius: 50%;
    background: var(--brand-ink);
  }
  .brand-name {
    font-size: 31px;
    line-height: 1.3;
    font-weight: 400;
  }
  .contact {
    position: absolute;
    right: 46px;
    top: 180px;
    text-align: right;
    color: var(--detail-ink);
  }
  .contact-name {
    font-size: 34px;
    color: var(--name-ink);
    letter-spacing: 0.5px;
    margin-right: 40px;
    margin-bottom: 40px;
    font-weight: 400;
  }
  .contact-line {
    display: flex;
    justify-content: flex-end;
    align-items: center;
    gap: 14px;
    font-size: 22px;
    line-height: 40px;
    white-space: nowrap;
  }
  .contact-line svg {
    width: 24px;
    height: 24px;
    flex: none;
  }
  .contact-line .spacer { width: 24px; flex: none; }
  .address { margin-top: 16px; }
</style>
</head>
<body>
  <div class="business-card">
    <svg class="card-art" viewBox="0 0 960 548" aria-hidden="true">
      <defs>
        <linearGradient id="panelFill" x1="0" y1="0" x2="0.25" y2="1">
          <stop offset="0" stop-color="var(--panel-top)"/>
          <stop offset="0.4" stop-color="var(--panel-mid)"/>
          <stop offset="0.7" stop-color="var(--panel-low)"/>
          <stop offset="1" stop-color="var(--panel-bottom)"/>
        </linearGradient>
      </defs>
      <path d="M 330 0 C 480 120, 480 400, 262 548 L 960 548 L 960 0 Z" fill="url(#panelFill)"/>
      <path d="M 308 0 C 458 120, 458 400, 240 548" fill="none" stroke="var(--divider)" stroke-width="6"/>
    </svg>

    <div class="brand">
      <span class="brand-dot"></span>
      <p class="brand-name">Harbourline Lift<br>Safety Ltd</p>
    </div>

    <div class="contact">
      <h1 class="contact-name">MARCUS DELLOW</h1>
      <p class="contact-line">07712948305
        <svg viewBox="0 0 24 24"><path d="M6 3c1 0 2 2.5 2.5 4 .2.8-1 1.6-1.4 2.2 1.2 2.6 3.1 4.5 5.7 5.7.6-.4 1.4-1.6 2.2-1.4 1.5.5 4 1.5 4 2.5 0 1.6-1.7 3.5-3.4 3.5C10 19.5 4.5 14 4.5 6.4 4.5 4.7 5 3 6 3z" fill="var(--detail-ink)"/></svg>
      </p>
      <p class="contact-line">marcus_dellow@brightmail.example
        <svg viewBox="0 0 24 24"><rect x="2.5" y="6" width="19" height="13" rx="1.5" fill="var(--detail-ink)"/><path d="M3 7l9 7 9-7" fill="none" stroke="var(--panel-low)" stroke-width="1.6"/></svg>
      </p>
      <p class="contact-line address">14 Glanmore Ave
        <svg viewBox="0 0 24 24"><path d="M12 2a7 7 0 0 0-7 7c0 5 7 13 7 13s7-8 7-13a7 7 0 0 0-7-7zm0 9.5A2.5 2.5 0 1 1 12 6.5a2.5 2.5 0 0 1 0 5z" fill="var(--detail-ink)"/></svg>
      </p>
      <p class="contact-line">Marrowdale West Coast ll934qx<span class="spacer"></span></p>
    </div>
  </div>
</body>
</html>
```